Social Business Consultancy

Makoro Ventures is a start up consultancy but with a difference: were non-corporate. We work in the field of economic development in low income countries and we focus on entrepreneurship but with a social and or environmental mission.

The type of projects we work on are innovative, ground breaking, different, edgy and bold. We are young, determined, , unreasonnable and undeterred by challenges.
We want our website to convey these ideas.
Updates

Hello,

Could you please include the option of having the website in two languages. Thank you.

Please note that new files have been added to the project brief.

- FrontPage  Main Photo (Grey dirt Road)
- WordCloud Photo to be used on the home page (as a small image )

The website should keep these colour tones.

Thank you !

Hello,

Wireframes have been uploaded. Please use as an indication.

Thanks,
n.

Target Market(s)

Governments, development agencies, social investors, NGOs, banks and social entrepreneurs.

Industry/Entity Type

Consulting

Requirements
Must have
• We already have a logo and business cards (provided). We want the website to look professional, yet simple with a maximum of two or three colours. We want the look to be seamless. There is no need for too many boxes or categories.
Nice to have
• We want bold, edgy, modern  and professional look .
• Examples:
• http://www.brightlanecollective.org/
• http://www.pagemorph.com/
• http://www.tallyhiring.co.nz/
Should not have
• The design should not use old style fonts.

```html
<!DOCTYPE html>
<html lang="en">
<head>
<meta charset="utf-8">
<title>Makoro Ventures – Main and Inner Page</title>
<link rel="stylesheet" href="https://fonts.googleapis.com/css2?family=Questrial&family=Ubuntu:wght@500;700&family=Open+Sans:wght@400;700&display=swap">
<style>
:root{
  --green:#cbdc28;
  --green-dark:#a9b81c;
  --blue:#0094d4;
  --blue-light:#21b0ea;
  --blue-head:#1b9ad6;
  --grey-bar:#66676b;
  --text:#555;
  --text-dark:#3c3c3c;
  --rule:#d8d8d8;
  --box:#f8f8f8;
  --box-line:#cfcfcf;
}
*{margin:0;padding:0;box-sizing:border-box}
html,body{width:1200px;height:2486px;overflow:hidden;background:#fff}
body{position:relative;font-family:"Open Sans",Verdana,sans-serif;color:var(--text)}
.abs{position:absolute}

.page-title{position:absolute;left:0;width:1200px;text-align:center;font-family:"Ubuntu",sans-serif;font-weight:700;font-size:37px;letter-spacing:1px;color:var(--blue-head)}

.site{position:absolute;left:0;width:1200px}
.topbar{position:absolute;left:0;top:0;width:1200px;height:14px;background:var(--green)}
.util-tab{position:absolute;top:14px;height:25px;background:var(--green);font-family:"Questrial",sans-serif;font-size:14px;color:#4a4a4a;text-align:center;line-height:25px;border-radius:0 0 3px 3px}
.util-tab.about{left:878px;width:92px}
.util-tab.contact{left:992px;width:93px}
.brand{position:absolute;left:68px;top:56px;display:flex;align-items:center;gap:12px}
.brand-name{font-family:"Questrial",sans-serif;font-size:34px;color:#5b5b5b}
.brand-mark{width:36px;height:36px;background:var(--green)}
.mainnav{position:absolute;left:498px;top:104px;width:702px;height:44px;background:linear-gradient(#23ace6,#0089c9);display:flex}
.mainnav a{display:block;height:44px;line-height:46px;text-align:center;font-family:"Ubuntu",sans-serif;font-weight:500;font-size:13px;color:#fff;text-decoration:none;letter-spacing:.3px;border-right:1px solid rgba(255,255,255,.25)}
.mainnav a:nth-child(1){width:184px}
.mainnav a:nth-child(2){width:160px}
.mainnav a:nth-child(3){width:161px}
.mainnav a:nth-child(4){width:197px;border-right:0}
.band{position:absolute;left:0;width:1200px;height:8px;background:var(--grey-bar)}
.hero{position:absolute;left:0;top:156px;width:1200px;background:linear-gradient(#a9aeae 0%,#c4c3b6 22%,#d6c38e 40%,#cdb27a 60%,#dcc390 100%)}
.lang{position:absolute;width:127px;height:39px;background:linear-gradient(#3c3c3c,#1c1c1c);border-radius:0 0 4px 4px;color:#fff;font-family:"Ubuntu",sans-serif;font-weight:500;font-size:14px;text-align:center;line-height:37px}
.lang span{color:#999;margin:0 8px}

.section-title{position:absolute;font-family:"Questrial",sans-serif;font-size:28px;color:var(--blue-head);font-weight:400}
.lead{font-size:12px;font-weight:700;line-height:17.5px;color:var(--text-dark);letter-spacing:.2px}
.copy{font-size:12px;line-height:17.5px;color:#666}
.vrule{position:absolute;width:0;border-left:1px dotted var(--rule)}
.placeholder{position:absolute}
.cloud{background:linear-gradient(120deg,#c7cc5c 0%,#8f8f8f 35%,#3a3a3a 55%,#9a9a9a 75%,#5bb8e0 100%);opacity:.85}
.panel{position:absolute;background:var(--box);border:1px solid var(--box-line)}
.news-list{list-style:none;padding:16px 14px 0 12px}
.news-list li{position:relative;padding-left:17px;font-size:12px;line-height:13.5px;color:#666;margin-bottom:14px}
.news-list li::before{content:"»";position:absolute;left:0;top:-2px;font-size:15px;font-weight:700;color:#333}
.more{position:absolute;right:14px;bottom:12px;font-size:10px;color:#666}
.panel-head{font-family:"Ubuntu",sans-serif;font-weight:500;font-size:15px;color:#555;text-align:center;letter-spacing:.3px}
.field-label{font-size:11px;color:#555}
.field{background:#fff;border:1px solid #bbb}
.btn{position:absolute;height:19px;background:linear-gradient(#21a8e4,#0088c8);color:#fff;font-size:11px;font-weight:700;text-align:center;line-height:19px;letter-spacing:.5px;border-radius:2px}
.footer{position:absolute;left:0;width:1200px;height:41px;background:linear-gradient(#0088c8,#22aee8);color:#fff;font-size:11px;font-weight:700;text-align:center;line-height:41px;letter-spacing:.5px}

.sidebar{position:absolute;left:68px;top:1712px;width:194px;height:734px;background:var(--green)}
.sidenav{position:absolute;left:66px;width:198px;height:29px;background:#fff;border-bottom:3px solid var(--green-dark);box-shadow:0 1px 3px rgba(0,0,0,.25);font-family:"Questrial",sans-serif;font-size:16px;color:#444;line-height:28px;padding-left:18px}
.framed{box-shadow:0 0 0 4px #fff,0 1px 6px 4px rgba(0,0,0,.3)}
</style>
</head>
<body>

<h1 class="page-title" style="top:30px">MAIN PAGE</h1>

<div class="site" style="top:103px;height:535px">
  <div class="topbar"></div>
  <div class="util-tab about">About Us</div>
  <div class="util-tab contact">Contact Us</div>
  <div class="brand"><span class="brand-name">Makoro Ventures</span><span class="brand-mark"></span></div>
  <nav class="mainnav"><a>OUR APPROACH</a><a>OUR SERVICES</a><a>OUR PARTNERS</a><a>NEWS / EVENTS</a></nav>
  <div class="band" style="top:148px"></div>
  <div class="hero" style="height:331px" role="img" aria-label="Photograph of a dirt road running through dry golden grassland under a grey sky"></div>
  <div class="band" style="top:487px"></div>
  <div class="lang" style="left:1004px;top:495px">English<span>|</span>French</div>
</div>

<h2 class="section-title" style="left:68px;top:656px">Welcome to Makoro Ventures</h2>
<div class="abs" style="left:68px;top:706px;width:355px">
  <p class="lead">Lorem Ipsum is simply dummy text of the printing and typesetting industry. Lorem Ipsum has been the industry's standard dummy text ever since the 1500s, when an unknown printer took a galley of type and scrambled it to make a type specimen book.</p>
  <p class="copy" style="margin-top:17px">It has survived not only five centuries, but also the leap into electronic typesetting, remaining essentially unchanged. It was popularised in the 1960s with the release of Typeline sheets containing Lorem Ipsum passages, and more recently with desktop publishing software like Folio Layout including versions of Lorem Ipsum.</p>
</div>
<div class="placeholder" style="left:117px;top:967px;width:233px;height:150px;background:radial-gradient(ellipse at 55% 55%,#b8a68a 0%,#6f7a45 35%,#2d3320 80%);border-radius:3px" role="img" aria-label="Photograph of open hands holding fresh green herbs"></div>

<div class="vrule" style="left:434px;top:662px;height:490px"></div>

<h2 class="section-title" style="left:466px;top:656px">Areas of Work</h2>
<div class="placeholder cloud" style="left:466px;top:710px;width:335px;height:173px" role="img" aria-label="Word cloud of terms such as Social, business, Innovation, Entrepreneurship, People and Solutions"></div>

<div class="vrule" style="left:819px;top:662px;height:490px"></div>

<h2 class="section-title" style="left:850px;top:658px;font-size:25px">News/Events</h2>
<div class="panel" style="left:850px;top:709px;width:281px;height:220px">
  <ul class="news-list">
    <li>Lorem Ipsum is simply dummy text of the printing and typesetting industry.</li>
    <li>Lorem Ipsum has been the industry's standard dummy text ever since the 1500s.</li>
    <li>It was popularised in the 1960s with the release of Typeline sheets containing Lorem Ipsum.</li>
    <li>It was popularised in the 1960s with the release of Typeline.</li>
  </ul>
  <span class="more">More</span>
</div>
<div class="panel" style="left:850px;top:965px;width:281px;height:135px">
  <div class="panel-head" style="margin-top:13px">SIGNUP FOR NEWSLETTER</div>
  <div class="field-label" style="position:absolute;left:42px;top:48px;font-weight:700">Email Address:</div>
  <div class="field abs" style="left:40px;top:65px;width:202px;height:27px"></div>
  <div class="btn" style="left:102px;top:103px;width:77px">Signup</div>
</div>

<footer class="footer" style="top:1197px">Copyright © 2010 makoroventures.com. All Rights Reserved.&nbsp; Contact Us | Privacy Policy | Legal</footer>

<h1 class="page-title" style="top:1288px">INNER PAGE</h1>

<div class="site" style="top:1353px;height:400px">
  <div class="topbar"></div>
  <div class="util-tab about">About Us</div>
  <div class="util-tab contact">Contact Us</div>
  <div class="brand"><span class="brand-name">Makoro Ventures</span><span class="brand-mark"></span></div>
  <nav class="mainnav"><a>OUR APPROACH</a><a>OUR SERVICES</a><a>OUR PARTNERS</a><a>NEWS / EVENTS</a></nav>
  <div class="band" style="top:146px"></div>
  <div class="hero" style="top:154px;height:197px" role="img" aria-label="Photograph of a dirt road running through dry golden grassland under a grey sky"></div>
  <div class="band" style="top:351px"></div>
</div>

<div class="sidebar"></div>
<div class="lang" style="left:1006px;top:1712px">English<span>|</span>French</div>
<div class="sidenav" style="top:1822px">What is Social Business</div>
<div class="sidenav" style="top:1860px">Our Approach</div>
<div class="sidenav" style="top:1898px">Our Services</div>
<div class="sidenav" style="top:1937px">Our Projects</div>
<div class="sidenav" style="top:1975px">Contact Us</div>

<h2 class="section-title" style="left:295px;top:1768px">Our Approach</h2>
<div class="abs" style="left:296px;top:1817px;width:480px">
  <p class="lead">Lorem Ipsum is simply dummy text of the printing and typesetting industry. Lorem Ipsum has been the industry's standard dummy text ever since the 1500s, when an unknown printer took a galley of type and scrambled it to make a type specimen book.</p>
  <p class="copy" style="margin-top:17px">It has survived not only five centuries, but also the leap into electronic typesetting, remaining essentially unchanged. It was popularised in the 1960s with the release of Typeline sheets containing Lorem Ipsum passages, and more recently with desktop publishing software like Folio Layout including versions of Lorem Ipsum.</p>
</div>

<h2 class="section-title" style="left:295px;top:2030px">Areas of Work</h2>
<p class="lead abs" style="left:296px;top:2082px;width:185px">Lorem Ipsum is simply dummy text of the printing and typesetting industry. Lorem Ipsum has been the industry's standard dummy text ever since the 1500s, when an unknown printer took a galley of type and scrambled it to make a type specimen book.</p>
<div class="placeholder cloud" style="left:483px;top:2085px;width:309px;height:160px" role="img" aria-label="Word cloud of terms such as Social, business, Innovation, Entrepreneurship, People and Solutions"></div>
<p class="copy abs" style="left:296px;top:2256px;width:480px">It has survived not only five centuries, but also the leap into electronic typesetting, remaining essentially unchanged. It was popularised in the 1960s with the release of Typeline sheets containing Lorem Ipsum passages, and more recently with desktop publishing software like Folio Layout including versions of Lorem Ipsum.</p>

<div class="vrule" style="left:811px;top:1760px;height:620px"></div>

<div class="placeholder framed" style="left:852px;top:1780px;width:277px;height:189px;background:linear-gradient(#dfe6e6 0%,#8d9488 30%,#5b5d52 60%,#3e3c36 100%)" role="img" aria-label="Photograph of a large banyan tree with hanging aerial roots"></div>

<h2 class="section-title" style="left:850px;top:2030px;font-size:25px">Contact Form</h2>
<div class="panel" style="left:850px;top:2071px;width:281px;height:320px">
  <div class="field-label abs" style="left:19px;top:18px">Name</div>
  <div class="field abs" style="left:19px;top:35px;width:233px;height:25px"></div>
  <div class="field-label abs" style="left:19px;top:72px">Email:</div>
  <div class="field abs" style="left:19px;top:89px;width:233px;height:25px"></div>
  <div class="field-label abs" style="left:19px;top:125px">Subject:</div>
  <div class="field abs" style="left:19px;top:142px;width:233px;height:25px"></div>
  <div class="field-label abs" style="left:19px;top:178px">Message:</div>
  <div class="field abs" style="left:19px;top:197px;width:233px;height:84px"></div>
  <div class="btn" style="left:68px;top:292px;width:65px">Submit</div>
  <div class="btn" style="left:145px;top:292px;width:64px">Clear</div>
</div>

<footer class="footer" style="top:2446px;height:40px;line-height:40px">Copyright © 2010 makoroventures.com. All Rights Reserved.&nbsp; Contact Us | Privacy Policy | Legal</footer>

</body>
</html>
```